Swift Heron Parcel & Delivery Services needs a flyer

We need an introductory flyer for a new company based in Yellowknife, Northwest Territories,Canada. Our company name is Swift Heron Parcel & Delivery Services. We will be handling envelopes and small packages up to 20 pounds. We expect 20 percent of our business to come from residential customers and 80 percent from the business community including lawyers, doctors, engineers and government offices. The main message that we will try to convey in this flyer is that we are a new and exciting company that promises to make 100% customer satisfaction our number one goal. I would like the layout to be elegant and simple and certainly not cluttered. It will be a single sided flyer. Text should be easy to read and most likely at most two fonts. I would like one stunning image or photo relating to the courier business and message. There should be plenty of white space throughout the flyer and nice margins on all sides. I would like my flyer to be 8.5 inches by 11 inches and it should read from top to bottom. . I would like a nice big bold headline that in some way mentions " Special Offer- Up to 100% Off. You can change the wording if you have a better idea. Throughout the flyer you can highlight and italicize for emphasis. Please try to use bullet points for my five main reasons for hiring our company which are: you will be 100% satisfied with each delivery or you will be given a complete refund no questions asked, your envelope or package will be delivered on time every time, you will always be treated throughout the delivery process in a professional manner, you will be given the widest selection in Yellowknife of price points and delivery options , you can trust us with your most important and time sensitive deliveries. Try to incorporate something next to these five points to really draw attention like a check mark, star etc.... I would prefer if my company name and contact info is in the bottom third of the flyer. My email is swiftheronparcelyk@mailbox-example.net. My phone number is 867-392-7184. It might be a good idea to have my phone number also at the top of the flyer someplace after the headline saying like Call Now!!! you can use boxes, borders and contrasting bold colors to bring flyer to life. I have a testimonial from a business owner that I dealt with when I ran another business which would be nice to have included . " While receiving daily deliveries for 18 years from Colin Marsh I found him to be punctual , reliable and efficient " Glen Hartley, owner of Hartley and Pruitt Supply LTD, Yellowknife,NWT. I thought perhaps at the top of flyer after the headline perhaps in some way you could say Yellowknife's newest and best courier and delivery service is pleased to offer the following stunning discounts: then you could list the three special offers: 1) First 5 businesses to book regular scheduled deliveries will get 100% off their first delivery. 2) First 5 businesses to book a single delivery will get 50% off that delivery. 3) First 5 residential customers to book a delivery will receive 25% off that delivery. I thought you could mention my name somewhere. Colin Marsh. Owner has lived in Yellowknife for 42 years and has 20 years experience doing performing important and time sensitive deliveries. Perhaps you could mention somewhere that we will have a couple of ongoing discounts also which will be 1) seniors discounts. 2) regular scheduled deliveries discounts. I have suggested colors but if you have other ideas I would certainly look at them. Our business tag line is. On Time Every Time
Target Market(s)
Business owners typically males 30-50 years old
Industry/Entity Type
Delivery Service
Requirements
Must have
- Done in CMYK mode sufficient bleed size for printing
Nice to have
- Nothing set in stone. I recently had my logo design uploaded to this brief. It is up to you if you feel it should be included in the flyer.
Should not have
- I am willing to look at any design

```html
<!DOCTYPE html>
<html lang="en">
<head>
<meta charset="utf-8">
<title>Swift Heron Parcel &amp; Delivery Services – Special Offer Flyer</title>
<link rel="stylesheet" href="https://fonts.googleapis.com/css2?family=Oswald:wght@500;600;700&family=Arimo:wght@400;700&family=Jost:wght@400;500&display=swap">
<style>
  :root {
    --navy: #2a2f7a;
    --crimson: #b3232f;
    --yellow: #f7e51c;
    --silver: #d9d9de;
    --white: #ffffff;
    --ink: #141414;
    --red-text: #d6202b;
    --photo-dark: #2b2b2e;
    --photo-mid: #8a6a55;
    --photo-light: #d9c5b0;
  }
  * { margin: 0; padding: 0; box-sizing: border-box; }
  html, body { width: 927px; height: 1200px; overflow: hidden; background: var(--white); }
  .flyer { position: relative; width: 927px; height: 1200px; background: var(--white); font-family: "Arimo", Arial, sans-serif; color: var(--ink); }

  .hero-photo {
    position: absolute; left: 0; top: 0; width: 450px; height: 440px;
    background: linear-gradient(120deg, var(--photo-light) 0%, var(--photo-mid) 35%, var(--photo-dark) 70%, #1a1a1c 100%);
  }
  .offer-panel {
    position: absolute; left: 450px; top: 0; width: 477px; height: 298px;
    background: var(--navy); text-align: center;
  }
  .offer-kicker { position: absolute; top: 26px; left: 0; right: 0; font-family: "Arimo", sans-serif; font-weight: 400; font-size: 34px; color: var(--yellow); padding-left: 60px; }
  .offer-upto { position: absolute; top: 56px; left: 0; right: 0; font-family: "Oswald", sans-serif; font-weight: 600; font-size: 72px; line-height: 1; color: var(--silver); padding-left: 60px; }
  .offer-amount { position: absolute; top: 130px; left: 0; right: 0; font-family: "Oswald", sans-serif; font-weight: 600; font-size: 150px; line-height: 1; color: var(--white); padding-left: 30px; letter-spacing: -2px; }
  .offer-amount small { font-size: 78px; }

  .call-panel {
    position: absolute; left: 450px; top: 298px; width: 477px; height: 142px;
    background: var(--crimson);
  }
  .call-now { position: absolute; top: 8px; left: 130px; font-family: "Oswald", sans-serif; font-weight: 600; font-size: 36px; color: var(--yellow); }
  .call-phone { position: absolute; top: 44px; left: -28px; font-family: "Oswald", sans-serif; font-weight: 700; font-size: 76px; line-height: 1.1; color: var(--white); letter-spacing: -1px; white-space: nowrap; }

  .intro { position: absolute; left: 30px; top: 448px; width: 870px; font-weight: 700; font-size: 19.5px; line-height: 1.25; }

  .discounts { position: absolute; left: 30px; top: 500px; width: 880px; list-style: none; font-size: 20px; line-height: 1.2; }
  .discounts li { position: relative; padding-left: 47px; margin-bottom: 2px; }
  .discounts .tick { position: absolute; left: 0; top: 2px; width: 42px; height: 22px; }
  .discounts .lead, .discounts .pct { color: var(--red-text); font-weight: 700; }
  .discounts .pct { font-size: 22px; }
  .discounts .wrap { display: block; padding-left: 110px; }

  .reasons { position: absolute; left: 238px; top: 618px; width: 470px; list-style: none; font-family: "Jost", sans-serif; font-size: 18px; line-height: 1.18; }
  .reasons li { position: relative; padding-left: 38px; margin-bottom: 15px; }
  .reasons li::before { content: ""; position: absolute; left: 0; top: 3px; width: 16px; height: 16px; border-radius: 50%; background: var(--crimson); }

  .ongoing-title { position: absolute; left: 30px; top: 880px; font-weight: 700; font-size: 20px; color: var(--navy); }
  .ongoing-band { position: absolute; left: 0; top: 909px; width: 927px; height: 34px; background: var(--navy); color: var(--white); font-weight: 700; font-size: 21px; line-height: 34px; padding-left: 105px; }
  .ongoing-band span::before { content: "\25CF"; margin-right: 8px; }
  .ongoing-band span + span { margin-left: 22px; }

  .brand { position: absolute; left: 0; right: 0; top: 962px; text-align: center; font-family: "Arimo", sans-serif; font-weight: 700; font-size: 40px; line-height: 1.15; color: var(--ink); }
  .email { position: absolute; left: 0; right: 0; top: 1076px; text-align: center; font-family: "Oswald", sans-serif; font-weight: 500; font-size: 31px; color: var(--navy); }

  .owner-band { position: absolute; left: 0; top: 1121px; width: 927px; height: 79px; background: var(--crimson); color: var(--white); text-align: center; font-family: "Oswald", sans-serif; font-weight: 500; font-size: 17.5px; line-height: 1.25; padding-top: 14px; }
  .owner-band strong { font-weight: 700; }
</style>
</head>
<body>
<main class="flyer">
  <div class="hero-photo" role="img" aria-label="Courier in a red shirt holding a cardboard parcel and a clipboard at a front door"></div>

  <section class="offer-panel">
    <p class="offer-kicker">Special Offer</p>
    <p class="offer-upto">Up to</p>
    <p class="offer-amount">100% <small>Off</small></p>
  </section>

  <section class="call-panel">
    <p class="call-now">Call Now!!!</p>
    <p class="call-phone">867-392-7184</p>
  </section>

  <p class="intro">Yellowknife's newest and best courier and delivery service is pleased to offer the following stunning discounts:</p>

  <ul class="discounts">
    <li><svg class="tick" viewBox="0 0 42 22"><path d="M2 12 L12 19 L40 3" fill="none" stroke="#d6202b" stroke-width="5" stroke-linecap="round" stroke-linejoin="round"/></svg><span class="lead">First 5</span> businesses to book regular scheduled deliveries will get <span class="pct">100% off</span> their <span class="wrap">first delivery.</span></li>
    <li><svg class="tick" viewBox="0 0 42 22"><path d="M2 12 L12 19 L40 3" fill="none" stroke="#d6202b" stroke-width="5" stroke-linecap="round" stroke-linejoin="round"/></svg><span class="lead">First 5</span> businesses to book a single delivery will get <span class="pct">50%</span> off that delivery.</li>
    <li><svg class="tick" viewBox="0 0 42 22"><path d="M2 12 L12 19 L40 3" fill="none" stroke="#d6202b" stroke-width="5" stroke-linecap="round" stroke-linejoin="round"/></svg><span class="lead">First 5</span> residential customers to book a delivery will receive <span class="pct">25%</span> off that delivery.</li>
  </ul>

  <ul class="reasons">
    <li>You will be 100% satisfied with each delivery or you will be given a complete refund no questions asked,</li>
    <li>Your envelope or package will be delivered on time every time,</li>
    <li>You will always be treated throughout the delivery process in a professional manner,</li>
    <li>You will be given the widest selection in Yellowknife of price points and delivery options</li>
    <li>You can trust us with your most important and time sensitive deliveries.</li>
  </ul>

  <p class="ongoing-title">Ongoing Discounts</p>
  <p class="ongoing-band"><span>Seniors Discounts</span><span>Regular Scheduled Deliveries Discounts</span></p>

  <p class="brand">Swift Heron<br>Parcel &amp; Delivery Services</p>
  <p class="email">swiftheronparcelyk@mailbox-example.net</p>

  <footer class="owner-band">
    <p><strong>Colin Marsh.</strong> Owner has lived in Yellowknife for 42 years and has 20 years experience<br>doing performing important and time sensitive deliveries.</p>
  </footer>
</main>
</body>
</html>
```